Professional Home Buyer business card needed

I need a pretty straight forward business card designed. We help people that NEED to sell their homes solve problems. We perform all types of Real Estate transactions including flip, wholesale, investment, rental property and multi family. The card will mainly be used to give to prospective Sellers but will also be given to Real Estate Investors as well. It should professional and very easy to read, most clients are older people.

Target Market(s)

Distressed home sellers as well as Real Estate investors

Industry/Entity Type

Real Estate

Contact Information for Business Card

should be a professional layout

Colors
ec1f27
ffffff
000000

Requirements
Must have
• Large logo on back and smaller one on front. should utilize Red, white, and black.
• I am thinking of using a soft touch coating on the card so keep that in mind.
• Contact info should be very easy to read, think older clients.
Nice to have
• I would like to see a design with rounded corners on the card
Should not have
• pictures of homes or other home graphics.

```html
<!DOCTYPE html>
<html lang="en">
<head>
<meta charset="utf-8">
<title>Keystone Home Buyers – Business Card</title>
<link rel="stylesheet" href="https://fonts.googleapis.com/css2?family=Saira:ital,wght@0,500;0,700;1,500;1,700&display=swap">
<style>
  :root {
    --brand-red: #ec1f27;
    --brand-white: #ffffff;
    --brand-black: #000000;
    --card-black: #0d0d0e;
    --backdrop: #2b2d31;
    --text-dark: #1a1a1a;
  }
  * { box-sizing: border-box; margin: 0; padding: 0; }
  html, body {
    width: 1200px; height: 900px; overflow: hidden;
    background: var(--backdrop);
    font-family: "Saira", sans-serif;
  }
  .canvas {
    position: relative; width: 1200px; height: 900px;
    display: flex; align-items: center; justify-content: center; gap: 40px;
  }
  .card {
    position: relative; width: 540px; height: 310px;
    border-radius: 16px; overflow: hidden;
    box-shadow: 0 14px 30px rgba(0,0,0,.45);
  }

  /* Brand name lockup: one colour, one weight, one square */
  .brand-lockup { display: flex; align-items: center; }
  .brand-mark { flex: none; background: var(--brand-red); }
  .brand-name { font-weight: 700; text-transform: uppercase; line-height: 1.05; }

  /* Back side */
  .card-back {
    background: var(--card-black);
    display: flex; align-items: center; justify-content: center;
  }
  .card-back .edge-stripe {
    position: absolute; left: 0; top: 0; bottom: 0; width: 14px;
    background: var(--brand-red);
  }
  .card-back .brand-lockup { gap: 20px; }
  .card-back .brand-mark { width: 22px; height: 22px; }
  .card-back .brand-name { font-size: 50px; color: var(--brand-white); }

  /* Front side */
  .card-front {
    background: var(--brand-white); color: var(--text-dark);
    padding: 28px 30px;
  }
  .person-name {
    font-weight: 700; font-style: italic; font-size: 30px;
    color: var(--brand-red); line-height: 1;
  }
  .person-title {
    font-weight: 500; font-style: italic; font-size: 22px;
    color: var(--text-dark); margin-top: 4px;
  }
  .contact-list { list-style: none; margin-top: 26px; }
  .contact-list li {
    display: flex; align-items: center; gap: 10px;
    font-size: 17px; font-weight: 500; line-height: 1.55;
  }
  .contact-list svg { width: 17px; height: 17px; flex: none; fill: var(--brand-red); }
  .front-logo { position: absolute; right: 30px; top: 30px; }
  .front-logo .brand-lockup { gap: 10px; }
  .front-logo .brand-mark { width: 12px; height: 12px; }
  .front-logo .brand-name { font-size: 20px; color: var(--brand-black); text-align: right; }
  .mail-address {
    position: absolute; right: 30px; bottom: 24px; text-align: right;
    font-size: 17px; font-weight: 500; line-height: 1.35; font-style: normal;
  }
</style>
</head>
<body>
<main class="canvas">

  <section class="card card-back" aria-label="Card back">
    <span class="edge-stripe"></span>
    <div class="brand-lockup">
      <span class="brand-mark"></span>
      <span class="brand-name">Keystone<br>Home Buyers</span>
    </div>
  </section>

  <section class="card card-front" aria-label="Card front">
    <h1 class="person-name">Daniel Hartwell</h1>
    <p class="person-title">President</p>

    <ul class="contact-list">
      <li>
        <svg viewBox="0 0 24 24" aria-hidden="true"><path d="M6.6 10.8a15.1 15.1 0 0 0 6.6 6.6l2.2-2.2a1 1 0 0 1 1-.25 11.4 11.4 0 0 0 3.6.57 1 1 0 0 1 1 1V20a1 1 0 0 1-1 1A17 17 0 0 1 3 4a1 1 0 0 1 1-1h3.5a1 1 0 0 1 1 1c0 1.25.2 2.45.57 3.57a1 1 0 0 1-.25 1z"/></svg>
        555-014-2386
      </li>
      <li>
        <svg viewBox="0 0 24 24" aria-hidden="true"><path d="M2 5h20v2l-10 6L2 7zM2 9l10 6 10-6v10H2z"/></svg>
        daniel@plainsHomesForCash.com
      </li>
      <li>
        <svg viewBox="0 0 24 24" aria-hidden="true"><path d="M12 2a10 10 0 1 0 0 20 10 10 0 0 0 0-20zm6.9 9h-3a15.6 15.6 0 0 0-1.3-6A8 8 0 0 1 18.9 11zM12 4.1A13.4 13.4 0 0 1 13.9 11h-3.8A13.4 13.4 0 0 1 12 4.1zM9.4 5a15.6 15.6 0 0 0-1.3 6h-3A8 8 0 0 1 9.4 5zM5.1 13h3a15.6 15.6 0 0 0 1.3 6 8 8 0 0 1-4.3-6zM12 19.9A13.4 13.4 0 0 1 10.1 13h3.8A13.4 13.4 0 0 1 12 19.9zm2.6-.9a15.6 15.6 0 0 0 1.3-6h3a8 8 0 0 1-4.3 6z"/></svg>
        www.plainsHomesForCash.com
      </li>
    </ul>

    <div class="front-logo">
      <div class="brand-lockup">
        <span class="brand-mark"></span>
        <span class="brand-name">Keystone<br>Home Buyers</span>
      </div>
    </div>

    <address class="mail-address">
      P.O. Box 112<br>Fairview, KS 67010
    </address>
  </section>

</main>
</body>
</html>
```